Essential oil label for bottles

Looking to modify our current logo and label design. It looks too simple. I will attach images of our competitors to use as examples. Our company name is Velnora. We have 2 different bottles. Clear and amber color. Going forward, we will be using only the amber bottle. The other 2 images are the biggest sellers brands. We want to make some adjustments to ours.

Target Market(s)

Brindex sales

Industry/Entity Type

Essential oil, perfume

Colors

Designer to choose only greyscale colors for use in the design.

Requirements
Nice to have
• A slight change to fonts and logo design. Maybe change the font and design of the word "Velnora" in our logo. Maybe add something to the label to make it stand out more but still keeping it clean and modern
Should not have
• No colors, besides, black, grays, whites, and off white.

```html
<!DOCTYPE html>
<html lang="en">
<head>
<meta charset="UTF-8">
<title>Velnora White Tea Fragrance Oil Label</title>
<link href="https://fonts.googleapis.com/css2?family=Montserrat:wght@800&family=Outfit:wght@300;400;500;600&display=swap" rel="stylesheet">
<style>
  :root {
    --page-bg: #f2f2f2;
    --label-bg: #f5f5f5;
    --ink: #111111;
    --rule: #6e6e6e;
    --contour-light: #ececec;
    --contour-mid: #dedede;
  }
  html, body {
    margin: 0;
    padding: 0;
    width: 1200px;
    height: 1092px;
    overflow: hidden;
    background: var(--page-bg);
  }
  .canvas {
    position: relative;
    width: 1200px;
    height: 1092px;
  }
  .label {
    position: absolute;
    left: 369px;
    top: 65px;
    width: 462px;
    height: 962px;
    background: var(--label-bg);
    box-shadow: 0 6px 18px rgba(0,0,0,0.08);
    overflow: hidden;
    font-family: "Outfit", sans-serif;
    color: var(--ink);
  }
  .contour {
    position: absolute;
  }
  .contour--top {
    right: 0;
    top: 0;
    width: 330px;
    height: 345px;
    background: radial-gradient(ellipse at 80% 50%, var(--contour-mid) 0%, var(--contour-light) 45%, var(--label-bg) 75%);
  }
  .contour--bottom {
    left: 0;
    bottom: 0;
    width: 462px;
    height: 70px;
    background: linear-gradient(180deg, var(--label-bg) 0%, var(--contour-light) 55%, var(--contour-mid) 100%);
  }
  .brand {
    position: absolute;
    left: 0;
    right: 0;
    top: 200px;
    display: flex;
    justify-content: center;
    align-items: center;
    gap: 18px;
  }
  .brand__dot {
    width: 22px;
    height: 22px;
    border-radius: 50%;
    background: var(--ink);
  }
  .brand__name {
    font-weight: 500;
    font-size: 24px;
    letter-spacing: 0.32em;
    line-height: 1;
  }
  .product-name {
    position: absolute;
    left: 0;
    right: 0;
    top: 588px;
    margin: 0;
    text-align: center;
    font-family: "Montserrat", sans-serif;
    font-weight: 800;
    font-size: 66px;
    letter-spacing: -0.02em;
    line-height: 1;
  }
  .spec-table {
    position: absolute;
    left: 42px;
    top: 681px;
    width: 379px;
    border-collapse: collapse;
  }
  .spec-table td, .spec-table th {
    border: 1.5px solid var(--rule);
    text-align: center;
    padding: 0;
  }
  .spec-table__title {
    height: 51px;
    font-weight: 600;
    font-size: 30px;
    letter-spacing: -0.01em;
  }
  .spec-table__note {
    height: 36px;
    width: 33.33%;
    font-weight: 400;
    font-size: 19px;
  }
  .volume {
    position: absolute;
    left: 0;
    right: 0;
    top: 858px;
    text-align: center;
    font-weight: 500;
    font-size: 21px;
  }
</style>
</head>
<body>
<div class="canvas">
  <section class="label">
    <div class="contour contour--top" role="img" aria-label="Topographic contour line pattern"></div>
    <div class="contour contour--bottom" role="img" aria-label="Topographic contour line pattern"></div>

    <div class="brand">
      <span class="brand__dot"></span>
      <span class="brand__name">VELNORA</span>
    </div>

    <h1 class="product-name">WHITE TEA</h1>

    <table class="spec-table">
      <tr><th class="spec-table__title" colspan="3">FRAGRANCE OIL</th></tr>
      <tr>
        <td class="spec-table__note">White Tea</td>
        <td class="spec-table__note">Orange</td>
        <td class="spec-table__note">Palo Santo</td>
      </tr>
    </table>

    <div class="volume">200 ML</div>
  </section>
</div>
</body>
</html>
```